DEADLINE 4 JAN 2015 - Drama Movie POSTER

Title of movie " KORAL " - in English SUNSET, Koral is a Sanskrit language, we expect the font to be a little towards that influence ( ethnic )

STORY:
This movie is about one girl's life survival, played by actress ( MIRA HALVORSEN ) fighting her life out of leukemia, deceived in relationship, denying love, searching for her birth father and later kidnapped but saved.

GENRE:
Its a drama with twist of thriller in the end.

COUNTRIES INVOLVED:
Phuket islands in Thailand and Bali and city scenes in Jakarta, Singapore and Istanbul.

We upload photos of actors involved, and we CAN have them on the poster, you can be creative but yet keep it elegant and sophisticated, the movie is for an upmarket. So we dont want too much color. Sunset color mixed with dark or black is nice.

Look forward to see you creative design! Thanks so much!

ACTORS NAME:
- Rudy Pelangi
- Kit B Mayhew
- Tobias Wen
- K Trax
- Hendra Sulut
- Mateo Brunvelli
- Mira Halvorsen
- Sari Lynne
- Ayu Kemalasari
- Ruqaya
- Felix Moro
- Yos Latuheru
- Faustino Medeira

TITLE OF MOVIE:
KORAL - " we love, we cry, we fall but we survive "

If you need sample of promotional trailer, please request with your email address.

Please Check our Brief as we have edited and add some more information needed.Many thanks and look forward to your arts.Warm Regards,KorvoStage Pictures Added Sunday, December 21, 2014

Investors, Young Adults and Adults Crowds

Movie

• Ethnic

• Movie title and Quotes : " we love, we cry, we fall but we survive "
• ( with or without logo ) Production House:
• KorvoStage Pictures in collaboration with Glimmerax.Inc
• Director's name:
• Budi Sastro & Teguh Rambukasih
• Actor Names in order:
• Rudy Pelangi, Ktrax, Sari Lynne, Hendra Sulut, Tobias Wen, Ayu Kemalasari, Felix Moro, Kit B Mayhew, Ruqaya, Mateo Brunvelli, Yos Latuheru, Mira Halvorsen, Faustino Medeira
• Poster influences: Fallow Ridge
• If you want to use the same idea, you can use a silhouette of a girl
• from one of mira halvorsen's picture WITHOUT exposing her face

```html
<!DOCTYPE html>
<html lang="en">
<head>
<meta charset="utf-8">
<title>Koral – Movie Poster</title>
<link rel="stylesheet" href="https://fonts.googleapis.com/css2?family=Barlow:wght@500;600&family=Kumar+One&display=swap">
<style>
  :root {
    --sunset-deep: #b5161d;
    --sunset-mid: #e8452a;
    --sunset-glow: #f79a5a;
    --ink: #000000;
    --paper: #ffffff;
    --portrait-dark: #1a0c08;
    --portrait-warm: #6a2a18;
  }
  * { margin: 0; padding: 0; box-sizing: border-box; }
  html, body { width: 849px; height: 1200px; overflow: hidden; background: var(--ink); }
  .poster {
    position: relative;
    width: 849px; height: 1200px;
    overflow: hidden;
    background:
      radial-gradient(ellipse 70% 45% at 50% 60%, var(--sunset-glow) 0%, var(--sunset-mid) 45%, var(--sunset-deep) 100%);
    font-family: "Barlow", sans-serif;
    color: var(--paper);
  }
  .portrait { position: absolute; left: 0; top: 0; width: 849px; height: 620px; }
  .dark-field { position: absolute; left: 0; top: 0; width: 849px; height: 1200px; }
  .title {
    position: absolute; left: 30px; top: 440px; width: 790px;
    font-family: "Kumar One", serif;
    font-size: 250px; line-height: 1; letter-spacing: -6px;
    color: var(--ink); text-align: center;
  }
  .credit-top { position: absolute; top: 30px; font-size: 28px; font-weight: 500; line-height: 1.08; white-space: nowrap; }
  .story-by { left: 34px; }
  .collab { right: 38px; text-align: right; }
  .tagline {
    position: absolute; left: 118px; top: 740px;
    font-size: 44px; font-weight: 600; line-height: 1.02;
    white-space: nowrap;
  }
  .tagline .emphasis { font-size: 56px; display: block; }
  .crew {
    position: absolute; left: 683px; transform: translateX(-50%);
    text-align: center; font-weight: 500; white-space: nowrap;
  }
  .director { top: 806px; font-size: 31px; line-height: 1.1; }
  .photography { top: 860px; font-size: 29px; line-height: 1.08; }
  .starring-label { position: absolute; right: 40px; top: 966px; font-size: 29px; font-weight: 600; white-space: nowrap; }
  .studio {
    position: absolute; left: 40px; top: 1037px; width: 151px; height: 123px;
    background: var(--paper); color: var(--ink);
    display: flex; flex-direction: column; align-items: center; justify-content: center; gap: 10px;
    font-size: 18px; font-weight: 500; text-align: center; line-height: 1.1;
  }
  .studio .mark { width: 40px; height: 40px; border-radius: 50%; background: var(--ink); }
  .cast {
    position: absolute; top: 1038px; list-style: none;
    font-size: 20px; font-weight: 500; line-height: 1.15; text-align: right; white-space: nowrap;
  }
  .cast-a { right: 457px; }
  .cast-b { right: 261px; }
  .cast-c { right: 43px; }
</style>
</head>
<body>
<main class="poster">
  <svg class="portrait" viewBox="0 0 849 620" role="img" aria-label="Moody portrait of the lead actress with dark shoulder-length hair, blended into the sunset">
    <defs>
      <radialGradient id="portraitTone" cx="50%" cy="40%" r="60%">
        <stop offset="0%" stop-color="#6a2a18" stop-opacity="0.85"/>
        <stop offset="70%" stop-color="#1a0c08" stop-opacity="0.9"/>
        <stop offset="100%" stop-color="#1a0c08" stop-opacity="0"/>
      </radialGradient>
    </defs>
    <path d="M250 560 C235 420 240 260 280 150 C320 40 410 10 440 10 C520 15 580 90 600 200 C620 320 600 450 560 560 Z" fill="url(#portraitTone)"/>
  </svg>

  <svg class="dark-field" viewBox="0 0 849 1200" aria-hidden="true">
    <polygon points="849,612 849,1200 0,1200 0,1000" fill="#000000"/>
  </svg>

  <h1 class="title">koral</h1>

  <p class="credit-top story-by">A story by<br>Mira Halvorsen</p>
  <p class="credit-top collab">In collaboration<br>with Glimmerax.Inc</p>

  <p class="tagline">we love, we cry,<br>we fall, but we <span class="emphasis">survive</span></p>

  <p class="crew director">Directed by Budi Sastro</p>
  <p class="crew photography">Director of photography:<br>Teguh Rambukasih</p>

  <p class="starring-label">Starring:</p>

  <div class="studio"><span class="mark"></span><span>KorvoStage<br>Pictures</span></div>

  <ul class="cast cast-a">
    <li>- Rudy Pelangi</li>
    <li>- Tobias Wen</li>
    <li>- Kit B Mayhew</li>
    <li>- Mira Halvorsen</li>
  </ul>
  <ul class="cast cast-b">
    <li>- Ktrax</li>
    <li>- Sari Lynne</li>
    <li>- Ayu Kemalasari</li>
    <li>- Mateo Brunvelli</li>
    <li>- Ruqaya</li>
  </ul>
  <ul class="cast cast-c">
    <li>- Hendra Sulut</li>
    <li>- Felix Moro</li>
    <li>- Yos Latuheru</li>
    <li>- Faustino Medeira</li>
  </ul>
</main>
</body>
</html>
```